Bright Ridge Electric Needs A Logo Design

We need a logo for my new company based out of Sacramento, Ca called Bright Ridge Electric. The name says it all, my electrical contracting business provides "Bright Ridge Professional Work" I'm open to any colors that pop and customers to say Wow. I would love to print my cards on metal.

Industry/Entity Type

Business

Contact Information for Business Card

The card needs to have as follows
Name of company: Bright Ridge Electric
My Name: Dorian Pelko
Phone # 916-382-5507
CL# 2087396
Email: brightridgeelectric@mailvance.net
and a slogan that represent "BRIGHT RIDGE"

Requirements
Must have
• The card needs to have as follows
• Name of company: Bright Ridge Electric
• My Name : Dorian Pelko
• Phone # 916-382-5507
• CL# 2087396
• Email: brightridgeelectric@mailvance.net
• and a slogan that represent "BRIGHT RIDGE"
Nice to have
• popping colors
• electrical Arcing

```html
<!DOCTYPE html>
<html lang="en">
<head>
<meta charset="utf-8">
<title>Bright Ridge Electric – Business Card</title>
<link rel="stylesheet" href="https://fonts.googleapis.com/css2?family=Open+Sans:wght@400;600;700&display=swap">
<style>
  :root {
    --backdrop: #3a3330;
    --card-black: #050505;
    --card-glow: #1c1c1c;
    --brand-blue: #0d5fd0;
    --text-white: #f2f2f2;
    --text-grey: #8a8a8a;
    --tab-silver: #d8d8d8;
  }
  * { margin: 0; padding: 0; box-sizing: border-box; }
  html, body {
    width: 1200px;
    height: 844px;
    overflow: hidden;
    background: var(--backdrop);
    font-family: "Open Sans", Arial, sans-serif;
  }
  .canvas {
    position: relative;
    width: 1200px;
    height: 844px;
  }
  .card {
    position: absolute;
    top: 272px;
    width: 525px;
    height: 300px;
    background: var(--card-black);
    box-shadow: 0 14px 30px rgba(0,0,0,0.55);
    overflow: hidden;
  }

  /* Contact side */
  .card-contact { left: 45px; background: linear-gradient(100deg, var(--card-black) 0%, #111 60%, var(--card-black) 100%); }
  .band {
    position: absolute;
    left: 0;
    width: 100%;
    height: 14px;
    background: var(--brand-blue);
  }
  .band-top { top: 0; }
  .band-bottom { bottom: 0; }
  .contact-block {
    position: absolute;
    top: 62px;
    left: 0;
    width: 100%;
    text-align: center;
    color: var(--text-white);
  }
  .person-name {
    font-size: 17px;
    font-weight: 700;
    margin-bottom: 10px;
  }
  .contact-line {
    display: flex;
    align-items: center;
    justify-content: center;
    gap: 6px;
    font-size: 13px;
    line-height: 22px;
  }
  .contact-line svg { width: 11px; height: 11px; fill: var(--text-white); }
  .slogan {
    margin-top: 26px;
    font-size: 16px;
    font-weight: 600;
    color: var(--brand-blue);
    letter-spacing: 0.3px;
    text-transform: uppercase;
  }

  /* Brand side */
  .card-brand {
    left: 630px;
    background: radial-gradient(ellipse at 55% 35%, var(--card-glow) 0%, var(--card-black) 70%);
  }
  .edge-tab {
    position: absolute;
    width: 34px;
    height: 40px;
    background: var(--brand-blue);
  }
  .edge-tab::after {
    content: "";
    position: absolute;
    top: 0;
    width: 5px;
    height: 100%;
    background: var(--tab-silver);
  }
  .edge-tab-left { left: 0; top: 186px; }
  .edge-tab-left::after { right: 0; }
  .edge-tab-right { right: 0; top: 40px; }
  .edge-tab-right::after { left: 0; }
  .brand-lockup {
    position: absolute;
    top: 96px;
    left: 0;
    width: 100%;
    display: flex;
    flex-direction: column;
    align-items: center;
    gap: 14px;
  }
  .brand-square {
    width: 44px;
    height: 44px;
    background: var(--brand-blue);
  }
  .brand-name {
    font-size: 28px;
    font-weight: 400;
    color: var(--text-grey);
    letter-spacing: 0.2px;
  }
</style>
</head>
<body>
<main class="canvas">

  <section class="card card-contact" aria-label="Business card contact side">
    <div class="band band-top"></div>
    <div class="contact-block">
      <p class="person-name">Dorian Pelko</p>
      <p class="contact-line">
        <svg viewBox="0 0 24 24" aria-hidden="true"><path d="M6.6 10.8a15.1 15.1 0 0 0 6.6 6.6l2.2-2.2a1 1 0 0 1 1-.25 11.4 11.4 0 0 0 3.6.57 1 1 0 0 1 1 1V20a1 1 0 0 1-1 1A17 17 0 0 1 3 4a1 1 0 0 1 1-1h3.5a1 1 0 0 1 1 1c0 1.25.2 2.45.57 3.6a1 1 0 0 1-.25 1z"/></svg>
        916-382-5507
      </p>
      <p class="contact-line">
        <svg viewBox="0 0 24 24" aria-hidden="true"><path d="M7 1h10a2 2 0 0 1 2 2v18a2 2 0 0 1-2 2H7a2 2 0 0 1-2-2V3a2 2 0 0 1 2-2zm0 3v14h10V4zm5 15.5a1 1 0 1 0 0 2 1 1 0 0 0 0-2z"/></svg>
        2087396
      </p>
      <p class="contact-line">
        <svg viewBox="0 0 24 24" aria-hidden="true"><path d="M2 5h20v14H2zm2 2v.5l8 5 8-5V7zm0 2.8V17h16V9.8l-8 5z"/></svg>
        brightridgeelectric@mailvance.net
      </p>
      <p class="slogan">Bright Ridge Professional Work</p>
    </div>
    <div class="band band-bottom"></div>
  </section>

  <section class="card card-brand" aria-label="Business card brand side">
    <div class="edge-tab edge-tab-right"></div>
    <div class="edge-tab edge-tab-left"></div>
    <div class="brand-lockup">
      <div class="brand-square"></div>
      <p class="brand-name">Bright Ridge Electric</p>
    </div>
  </section>

</main>
</body>
</html>
```